Corwith Lodge website redesign

After 8 years of our current site, we're ready to upgrade our site design. We'd like to generally make it more modern and clean and build it on a CMS like joomla for easier future maintenance.

Our hotel is a family-owned bed and breakfast that competes against much larger hotel chains in Aspen with fancier rooms and larger pricetags. Our hotel is priced moderately and features tasteful, uniquely-design rooms.

We are looking for a website that will showcase the uniqueness of our rooms, the history of the Lodge, and the friendliness of our staff.

Here are some other hotel sites we like:

http://www.brackenfoldhouse.example/

http://www.tollerpeakhaus.example/

http://www.quarrowstay.example/

*********

Scope of Work - I'm looking for a design AND build. The website should be built out in Joomla as part of the final deliverable.
Updates

Current website: http://www.corwithlodge.example/

Explanation of what design + build means:

I am looking for not only the design of the site, but also for the homepage and one subpage to be built out as well. I do NOT need the entire site built - only for those two pages to be built and I will retrofit the remainder of the pages.

Target Market(s)

travellers evaluating hotels in Aspen, Colorado.

Industry/Entity Type

Hotel

Requirements
Must have
• Must, must, must be based on a joomla template. "Rotating" large main image as central position on homepage is a must (see example websites mentioned above).

Nice to have
• We have an existing online reservation system. It would be nice to evaluate placing a "widget" on the homepage that integrates to the online reservation page. Similar to that feature that the Bracken Fold website has at the foot of the main image on their homepage.

```html
<!DOCTYPE html>
<html lang="en">
<head>
<meta charset="utf-8">
<title>Corwith Lodge – Aspen Colorado</title>
<link rel="stylesheet" href="https://fonts.googleapis.com/css2?family=Maven+Pro:wght@400;500&family=Arimo:wght@400;700&display=swap">
<style>
:root{
  --page:#ffffff;
  --text-rust:#8a3a26;
  --heading-rust:#8b2f1c;
  --footer-rust:#953d28;
  --footer-text:#f1ddd5;
  --footer-muted:#d79a86;
  --strip-dark:#262626;
  --nav-blue:#1d4a86;
  --nav-blue-dark:#123262;
  --input-dark:#2b2b2b;
}
*{box-sizing:border-box;margin:0;padding:0}
html,body{width:763px;height:1200px;overflow:hidden;background:var(--page)}
body{position:relative;font-family:"Arimo",Arial,sans-serif;color:var(--text-rust)}
.hero{position:absolute;left:0;top:0;width:763px;height:451px;
  background:linear-gradient(180deg,#2f6fd8 0%,#5b8fd8 14%,#5a6f84 24%,#2d3d36 34%,#1d2d22 55%,#22331f 72%,#3c3a1e 86%,#b5771f 94%,#7a5a22 100%)}
.slide-dots{position:absolute;top:390px;left:360px;display:flex;gap:28px}
.slide-dots span{width:7px;height:7px;border-radius:50%;border:1px solid rgba(255,255,255,.6)}
.slide-dots span.active{background:rgba(255,120,80,.8)}
.site-header{position:absolute;left:0;top:11px;width:763px;height:49px;
  background:linear-gradient(180deg,var(--nav-blue) 0%,var(--nav-blue-dark) 100%);opacity:.93;
  border-top:2px solid #3a78c8}
.brand{position:absolute;left:74px;top:10px;font-family:"Maven Pro",sans-serif;font-weight:400;font-size:25px;color:#fff;letter-spacing:.5px}
.main-nav{position:absolute;right:57px;top:20px;display:flex}
.main-nav a{font-family:"Maven Pro",sans-serif;font-size:9px;color:#fff;text-decoration:none;padding:0 14px;border-left:1px solid rgba(255,255,255,.15);position:relative;text-transform:uppercase}
.main-nav a:first-child{border-left:0}
.main-nav a.has-sub::after{content:"";position:absolute;left:50%;top:15px;margin-left:-2px;border:2px solid transparent;border-top:3px solid #cfd9e8}
.welcome{position:absolute;left:0;top:451px;width:763px;height:70px;background:linear-gradient(180deg,#f2f2f2,#fff)}
.welcome h1{position:absolute;top:20px;width:100%;text-align:center;font-family:"Maven Pro",sans-serif;font-weight:500;font-size:14.5px;color:var(--heading-rust);letter-spacing:.8px;text-transform:uppercase}
.welcome .rule{position:absolute;left:72px;right:72px;top:55px;height:1px;background:#e8e8e8}
.about{position:absolute;left:70px;top:531px;width:622px;font-size:8.6px;line-height:13.4px}
.about p{margin-bottom:9px}
.photo{border-radius:6px}
.photo-lodge{float:left;width:291px;height:186px;margin:22px 14px 2px 6px;
  background:linear-gradient(180deg,#d9e2ea 0%,#6b5a3f 35%,#7a4a26 65%,#3c2a1c 100%)}
.photo-lounge{float:right;width:189px;height:142px;margin:2px 5px 0 18px;
  background:linear-gradient(180deg,#6a4a2c 0%,#8a5e34 45%,#5a3a22 100%)}
.content-shadow{position:absolute;left:95px;right:70px;top:932px;height:4px;border-radius:50%;background:radial-gradient(ellipse at center,rgba(0,0,0,.18),transparent 70%)}
.to-top{position:absolute;right:1px;width:15px;height:15px;background:#1d1d1d;border:1px solid #555}
.to-top::after{content:"";position:absolute;left:3px;top:4px;border:4px solid transparent;border-bottom:4px solid #fff;border-top:0}
.site-footer{position:absolute;left:0;top:938px;width:763px;height:178px;background:var(--footer-rust)}
.footer-col{position:absolute;top:27px}
.footer-col h2{font-family:"Maven Pro",sans-serif;font-weight:500;font-size:8.6px;color:#fff;text-transform:uppercase;margin-bottom:13px}
.footer-menu{left:70px}
.footer-menu ul{list-style:none}
.footer-menu li{font-size:8.2px;color:var(--footer-text);line-height:13.4px}
.mailing{left:282px}
.mailing .field{width:121px;height:18px;background:var(--input-dark);border-radius:3px;color:#ddd;font-size:7.8px;padding:5px 5px;margin-bottom:10px;box-shadow:inset 0 1px 2px rgba(0,0,0,.6)}
.mailing .subscribe{display:inline-block;background:#6d3b2f;color:#e6cfc6;font-size:7.8px;padding:3px 8px;border-radius:3px;border:1px solid #5a2e24}
.contact{left:494px;font-size:7.8px;line-height:13.3px;color:var(--footer-muted)}
.contact .maps{margin-top:12px;color:#fff;display:flex;align-items:center;gap:5px}
.footer-strip{position:absolute;left:0;top:1116px;width:763px;height:13px;background:var(--strip-dark)}
.footer-bottom{position:absolute;left:0;top:1129px;width:763px;height:71px;background:var(--footer-rust)}
.footer-brand{position:absolute;left:72px;top:12px;display:flex;align-items:center;gap:6px;font-family:"Maven Pro",sans-serif;font-size:15px;color:#f4e4dc}
.footer-brand i{width:9px;height:9px;border-radius:50%;background:#c98e7c;display:block}
.copyright{position:absolute;left:79px;top:37px;font-size:7px;color:#d9a090}
.share{position:absolute;top:12px;left:422px;display:flex;gap:8px}
.share span{font-size:7px;height:14px;padding:3px 5px;border-radius:2px;background:#f2f2f2;color:#334;border:1px solid #bbb}
.share span.dark{background:#3a3a3a;color:#fff;border-color:#222;font-weight:700}
</style>
</head>
<body>
<div class="hero" role="img" aria-label="Photograph of pine forest and mountain lake near Aspen with autumn foliage"></div>
<div class="slide-dots"><span></span><span class="active"></span></div>

<header class="site-header">
  <div class="brand">Corwith Lodge</div>
  <nav class="main-nav">
    <a class="has-sub">Home</a>
    <a class="has-sub">Sliders</a>
    <a>Blog</a>
    <a>Contact</a>
  </nav>
</header>

<section class="welcome">
  <h1>Welcome to the Corwith Lodge - Aspen Colorado.</h1>
  <div class="rule"></div>
</section>

<main class="about">
  <div class="photo photo-lodge" role="img" aria-label="Photograph of the lodge exterior in snow with clock on the gable"></div>
  <p>Located in the heart of downtown Aspen, the newly renovated Corwith Lodge possesses all the charms of a vintage European Ski Lodge, while offering all of the modern conveniences one would expect with a stay in Aspen.</p>
  <p>A stay at our lodge includes free continental breakfast in our dining room, daily maid service, free wireless internet access, and a fully-equipped conference facility. Guests are also invited to relax in one of our two outdoor hot tubs or in our lounge, where a 42-inch plasma TV and fireplace make for a pleasant area to unwind.</p>
  <p>The Corwith Lodge was founded in 1948 and has been a local favorite ever since. It was originally known as the Hearthside Lodge and was renamed in 2005. As a family-owned lodge, we take pride in maintaining a comfortable home away from home in beautiful Aspen, Colorado. The lodge has 35 guest rooms and each room is uniquely decorated with specially chosen furniture and tiles that give the feel of luxury. Every room has a flat panel television with cable, high speed internet access via ethernet cable and via wireless connection, and CD player clock radios. Each morning of your stay you will be treated to a buffet breakfast that is included with your room. Then just walk outside and catch the free shuttle bus to Hollin Peak or Tarnfield. It's a quick ride from our door to the Hollin Peak Gondola.</p>
  <div class="photo photo-lounge" role="img" aria-label="Photograph of the wood-panelled breakfast lounge"></div>
  <p>And after a long day of skiing, mountain biking, or hiking, you may relax in our hot tub with great views of Hollin Peak and Redcrest Ridge, or enjoy freshly baked cookies in front of our lobby fireplace or our courtyard firepit. Our staff will assist you in discovering all that Aspen has to offer from the best restaurants in town to great places for summer and winter activities. We look forward to seeing you at the Corwith Lodge, where every day is a holiday.</p>
</main>
<div class="content-shadow"></div>
<a class="to-top" style="top:844px" aria-label="Back to top"></a>

<footer class="site-footer">
  <div class="footer-col footer-menu">
    <h2>Footer Menu</h2>
    <ul>
      <li>Vestibulum ante</li>
      <li>Felis odio</li>
      <li>Suspendisse fringilla</li>
      <li>Consequat venenatis</li>
      <li>Quis mauris</li>
      <li>Aliquam felis</li>
    </ul>
  </div>
  <div class="footer-col mailing">
    <h2>Join our mailing list</h2>
    <div class="field">Your name</div>
    <div class="field">Your email address</div>
    <span class="subscribe">Subscribe</span>
  </div>
  <div class="footer-col contact">
    <h2>Contact Details</h2>
    The Corwith Lodge<br>
    418 W. Hollin Street Aspen,<br>
    CO 81611<br>
    Phone: 970-555-0142<br>
    Toll Free: 877-555-0187 (877-CORW LDG)<br>
    Fax: 970-555-0163
    <div class="maps">
      <svg width="6" height="8" viewBox="0 0 6 8"><path d="M3 0a3 3 0 0 0-3 3c0 2 3 5 3 5s3-3 3-5a3 3 0 0 0-3-3zm0 4.2a1.2 1.2 0 1 1 0-2.4 1.2 1.2 0 0 1 0 2.4z" fill="#fff"/></svg>
      We on Maps
    </div>
  </div>
</footer>
<div class="footer-strip"></div>
<a class="to-top" style="top:1119px" aria-label="Back to top"></a>
<div class="footer-bottom">
  <div class="footer-brand"><i></i>Corwith Lodge</div>
  <div class="copyright">Copyright 2012 The Corwith Lodge - All rights are reserved</div>
  <div class="share">
    <span class="dark">Comments</span>
    <span>Like 0</span>
    <span>+1 0</span>
    <span>Share 1</span>
  </div>
</div>
</body>
</html>
```